Complete Stationary Package Needed for New Dental Office ! ! !

I'm moving my dental office and would like to use my existing logo to create a new:
- Business Card (please submit Business Card designs to this project - http://tasks.artbidhub.example/task.aspx?id=514290)
- Appointment Card (submit here)
- Letterhead (submit here)
- Envelope (submit here)
My practice name (within my logo) is:
Melvin R. Tuttle, D.D.S., P.A.
Family and Cosmetic Dentistry
***Obviously you will notice that the lower leg of the "T" in my logo is a smile.
My new address and contact information is:
340 Larkspur Commons Drive, Suite 118
Cary, NC 27593
919-472-3081 (ph)
919-472-3095 (fax)
info@tuttledds.example
www.tuttledds.example
If you would like to use a tagline, I would suggest "Careful Dentistry with a Gentle Hand".
I have attached my logo in numerous formats.
I have also attached 2 QR codes, one of which links to my website and the other one which links to a "Like" page for my business Chatterly page. These QR codes could be improved by putting a graphic in the middle, but I created these myself and did not know how to do this.
Thank you for your time. I look forward to seeing all of your creative ideas!
Depending on the designs, I may award 2 different winners for the Business Card project and the Stationery Project. Or if a design is really good, I will award both projects to the same designer.
Updates
Project Deadline Extended
Reason: PixelBazaar administrators recently helped me split my project into 2 projects - 1 for business card and 1 for letterhead, envelope, etc. and I would like sufficient time to receive designs and provide feedback. Thank you.
Target Market(s)
Current and prospective dental patients.
Industry/Entity Type
Dental
Requirements
Must have
- Please ensure business card has a 2-sided design.
- Please ensure that your design is "practical" for printing purposes.
Nice to have
- Improvement of QR codes by addition of graphics in the middle to differentiate them. Incorporation of QR codes into business card design, maybe on the back side? I would consider the Chatterly QR code more important than the website QR code simply because my website URL is very easy to type.
Should not have
- Please, NO "floating" or "extracted" teeth which sends an undesirable message.

```html
<!DOCTYPE html>
<html lang="en">
<head>
<meta charset="utf-8">
<title>Melvin R. Tuttle, D.D.S., P.A. — Letterhead</title>
<link rel="stylesheet" href="https://fonts.googleapis.com/css2?family=Cinzel:wght@600&family=Crimson+Pro:wght@400;500&display=swap">
<style>
  :root {
    --backdrop: #edeeee;
    --paper: #ffffff;
    --navy: #232a78;
    --navy-deep: #141746;
    --teal: #0d6a68;
    --teal-text: #0e5a5a;
    --rule: #1f3a5e;
    --white: #ffffff;
  }
  * { margin: 0; padding: 0; box-sizing: border-box; }
  html, body { width: 1200px; height: 900px; overflow: hidden; background: var(--backdrop); }
  .letterhead {
    position: absolute; left: 310px; top: 40px;
    width: 580px; height: 820px;
    background: var(--paper);
    overflow: hidden;
    box-shadow: 0 1px 3px rgba(0,0,0,0.08);
  }
  .header-band, .footer-band { position: absolute; left: 0; width: 580px; }
  .header-band { top: 0; height: 80px; }
  .footer-band { bottom: 0; height: 80px; }
  .brand-mark {
    position: absolute; left: 35px; top: 44px;
    width: 72px; height: 72px;
    background: var(--navy);
    border: 2px solid var(--white);
    outline: 1px solid var(--teal);
  }
  .practice { position: absolute; left: 144px; top: 44px; }
  .practice-name {
    font-family: "Cinzel", serif; font-weight: 600;
    font-size: 15px; color: var(--navy); letter-spacing: 0.3px;
    border-bottom: 1px solid var(--navy); padding-bottom: 1px;
  }
  .practice-tagline {
    font-family: "Cinzel", serif; font-weight: 600;
    font-size: 8px; color: var(--teal-text); letter-spacing: 1px;
    text-align: center; margin-top: 2px;
  }
  .address {
    position: absolute; left: 144px; top: 90px;
    font-family: "Crimson Pro", serif; font-style: normal;
    font-size: 12.5px; line-height: 17px;
    color: var(--teal-text);
  }
  .contact {
    position: absolute; right: 28px; top: 60px;
    list-style: none;
    font-family: "Crimson Pro", serif; font-size: 12.5px; color: var(--teal-text);
  }
  .contact li { display: flex; justify-content: flex-end; align-items: center; height: 21px; gap: 9px; }
  .contact svg { width: 14px; height: 14px; flex: none; }
  .header-rule {
    position: absolute; left: 34px; top: 128px; width: 511px;
    border-top: 1.3px solid var(--rule);
  }
  .footer-tagline {
    position: absolute; left: 184px; bottom: 14px;
    font-family: "Crimson Pro", serif; font-size: 12px; color: var(--white);
  }
  .footer-brand {
    position: absolute; right: 14px; bottom: 10px;
    display: flex; align-items: center; gap: 4px;
  }
  .footer-brand-name {
    font-family: "Cinzel", serif; font-weight: 600; font-size: 6px;
    color: var(--white); letter-spacing: 0.2px;
  }
  .footer-brand-mark { width: 17px; height: 17px; border: 1px solid var(--white); background: var(--navy); }
</style>
</head>
<body>
  <main class="letterhead">
    <svg class="header-band" viewBox="0 0 580 80" preserveAspectRatio="none" aria-hidden="true">
      <defs>
        <linearGradient id="headerFill" x1="0" y1="0" x2="1" y2="0">
          <stop offset="0" stop-color="#0c6a67"/>
          <stop offset="0.55" stop-color="#232a78"/>
          <stop offset="1" stop-color="#12153f"/>
        </linearGradient>
      </defs>
      <path d="M0,0 H580 V4 C540,22 490,44 400,42 C300,40 220,30 0,34 Z" fill="url(#headerFill)"/>
    </svg>

    <div class="brand-mark" aria-hidden="true"></div>
    <div class="practice">
      <div class="practice-name">Melvin R. Tuttle, D.D.S., P.A.</div>
      <div class="practice-tagline">Family and Cosmetic Dentistry</div>
    </div>
    <address class="address">
      340 Larkspur Commons Drive, Suite 118<br>
      Cary, NC 27593
    </address>
    <ul class="contact">
      <li>919-472-3081
        <svg viewBox="0 0 14 14" aria-hidden="true"><path d="M1,7 C1,3 13,3 13,7 L10,8 L10,6 L4,6 L4,8 Z M3,9 H11 L12,12 H2 Z" fill="#0e5a5a"/></svg>
      </li>
      <li>919-472-3095
        <svg viewBox="0 0 14 14" aria-hidden="true"><rect x="1.5" y="1" width="11" height="12" rx="1.5" fill="#0e5a5a"/><rect x="4" y="4" width="6" height="1.2" fill="#fff"/><rect x="4" y="7" width="6" height="1.2" fill="#fff"/></svg>
      </li>
      <li>www.tuttledds.example
        <svg viewBox="0 0 14 14" aria-hidden="true"><circle cx="7" cy="7" r="6" fill="#0e5a5a"/><path d="M1,7 H13 M7,1 V13 M3,3.5 H11 M3,10.5 H11" stroke="#fff" stroke-width="0.8" fill="none"/><ellipse cx="7" cy="7" rx="2.6" ry="6" stroke="#fff" stroke-width="0.8" fill="none"/></svg>
      </li>
    </ul>
    <div class="header-rule"></div>

    <svg class="footer-band" viewBox="0 0 580 80" preserveAspectRatio="none" aria-hidden="true">
      <defs>
        <linearGradient id="footerFill" x1="0" y1="0" x2="1" y2="0">
          <stop offset="0" stop-color="#14184a"/>
          <stop offset="0.5" stop-color="#232a78"/>
          <stop offset="1" stop-color="#0c6a67"/>
        </linearGradient>
      </defs>
      <path d="M0,36 C40,10 110,6 200,14 C320,26 420,22 580,12 V16 C420,28 320,32 200,22 C110,14 40,18 0,42 Z" fill="#0c6a67"/>
      <path d="M0,48 C40,22 110,18 200,26 C320,38 420,34 580,24 V80 H0 Z" fill="url(#footerFill)"/>
    </svg>
    <p class="footer-tagline">Careful Dentistry with a Gentle Hand</p>
    <div class="footer-brand">
      <span class="footer-brand-name">Melvin R. Tuttle, D.D.S., P.A.</span>
      <span class="footer-brand-mark" aria-hidden="true"></span>
    </div>
  </main>
</body>
</html>
```